Load Up Your Cart

Require two banners with a size of 980 x 450 pixels
Similar natural looking banner as per attachment. The background is supposed to be a cardboard carton
price "$9.95"
Wording and layout the same as attached file

```html
<!DOCTYPE html>
<html lang="en">
<head>
<meta charset="utf-8">
<title>Load Up Your Cart – Flat Rate Shipping</title>
<link rel="stylesheet" href="https://fonts.googleapis.com/css2?family=Saira+Stencil+One&family=Big+Shoulders+Stencil+Display:wght@800&family=Stardos+Stencil:wght@700&display=swap">
<style>
  :root {
    --kraft-light: #e6d6a6;
    --kraft-mid: #cdb985;
    --kraft-dark: #b39e68;
    --stamp-brown: #5b4a3a;
    --price-red: #dc1419;
  }
  html, body {
    margin: 0;
    padding: 0;
    width: 1200px;
    height: 551px;
    overflow: hidden;
  }
  .banner {
    position: relative;
    width: 1200px;
    height: 551px;
    background:
      radial-gradient(ellipse 420px 260px at 78% 22%, rgba(245,232,190,.75), transparent 70%),
      radial-gradient(ellipse 380px 240px at 30% 75%, rgba(242,228,185,.6), transparent 70%),
      radial-gradient(ellipse 360px 220px at 10% 15%, rgba(170,150,95,.45), transparent 70%),
      radial-gradient(ellipse 420px 220px at 60% 95%, rgba(175,155,100,.45), transparent 70%),
      radial-gradient(ellipse 300px 200px at 98% 80%, rgba(180,160,105,.4), transparent 70%),
      linear-gradient(100deg, var(--kraft-mid), var(--kraft-light) 45%, var(--kraft-mid));
  }
  .artwork {
    position: absolute;
    inset: 0;
    width: 1200px;
    height: 551px;
  }
  .stamp-ring { fill: none; stroke: var(--stamp-brown); stroke-width: 9; }
  .stamp-text {
    fill: var(--stamp-brown);
    font-family: "Saira Stencil One", "Arial Black", sans-serif;
  }
  .price {
    fill: var(--price-red);
    font-family: "Big Shoulders Stencil Display", Impact, sans-serif;
    font-weight: 800;
  }
  .shipping-label {
    fill: var(--price-red);
    font-family: "Stardos Stencil", "Courier New", serif;
    font-weight: 700;
  }
  .terms {
    fill: var(--stamp-brown);
    font-family: "Stardos Stencil", "Courier New", serif;
    font-weight: 700;
  }
</style>
</head>
<body>
  <main class="banner">
    <svg class="artwork" viewBox="0 0 1200 551" xmlns="http://www.w3.org/2000/svg">
      <g class="stamp" transform="rotate(-4 279 269)">
        <circle class="stamp-ring" cx="279" cy="269" r="231"/>
        <text class="stamp-text stamp-load" x="84" y="250" font-size="165" textLength="360" lengthAdjust="spacingAndGlyphs">LOAD</text>
        <text class="stamp-text stamp-up" x="118" y="418" font-size="180" textLength="162" lengthAdjust="spacingAndGlyphs">UP</text>
        <text class="stamp-text stamp-your" x="290" y="324" font-size="76" textLength="166" lengthAdjust="spacingAndGlyphs">YOUR</text>
        <text class="stamp-text stamp-cart" x="296" y="402" font-size="76" textLength="156" lengthAdjust="spacingAndGlyphs">CART</text>
      </g>
      <text class="price" x="649" y="251" font-size="218" textLength="374" lengthAdjust="spacingAndGlyphs">$9.95</text>
      <text class="shipping-label" x="539" y="393" font-size="72" textLength="606" lengthAdjust="spacingAndGlyphs">FLAT RATE SHIPPING</text>
      <text class="terms" x="471" y="490" font-size="50" textLength="716" lengthAdjust="spacingAndGlyphs">NO MINIMUMS. NO CODES. NO GIMMICKS.</text>
    </svg>
  </main>
</body>
</html>
```